Pull Up Banner - Recruitment Company

We would like a design for a pull up banner.

For context: we are a recruitment business. We specialise in helping people in healthcare industry to find jobs in Australia.

I have come up with several ideas and text for the banner. Feel free to use the following as you see appropriate:

- Our logo (see attached)
- 'Healthcare Recruitment Agency'
- Some sort of imagine / cartoon of medical professionals (ie. doctor, nurse, physiotherapist, speech pathologist). A cartoon is more friendly than committing to a photo
- 'Empowering your next career move'
- 'Discover tailored opportunities based on your career preferences'
- Dot points (allied health, nursing, medical imaging)
- Contact info at the bottom including our website (www.quellstaffing.com.au, our Instagram handle @quellstaffing, Mobile: XXXX XXX XXX. The title section for contact information could be 'Get in touch:'

Feel free to submit a couple of designs and we can merge aspects that look good on your designs and find the perfect fit.
Thank you
Updates

Hello,

Thank you for your initial submissions to this project. I appreciate the time you've invested.

After reviewing the first attempt, I'd like to share some feedback and initial observations:

- Professionalism and engagement: Is the overall appearance of the banner professional? It's crucial that we have a high-quality design as this will represent our business.

- Image selection: The image (whether cartoon or real people) appears quite generic. Please consider submitting the banner with a few different photos in the middle for us to choose from. Ensure the image is a good fit and not simply a generic stock photo.

- Contact section: Kindly remove the phone number; we no longer wish to include it on the banner. Instead, please include our website (www.quellstaffing.com.au) and Instagram handle (@quellstaffing).

- Color scheme: White, black, and red/pink are preferred, or alternatively, blue. However, please avoid incorporating too many different colors as it may detract from the professional appearance.

We will be printing the design on a banner and require it to look professional and engaging.

Thank you once again for your submissions. I hope the feedback provided above is helpful.

Warm regards,

Target Market(s)

Allied Health Australia

Font styles to use
Serif

Colors
0054AA
0677BA
7BADD7
CADEEF
E8F1F8
0094D4
00A9DD
6FCCEA
C7EBF8
E9F6FB
EB3D1F
EC4F4E
F09395
F8D3D4
FCEDEE

```html
<!DOCTYPE html>
<html lang="en">
<head>
<meta charset="utf-8">
<title>Quell Staffing – Pull Up Banner</title>
<link rel="stylesheet" href="https://fonts.googleapis.com/css2?family=Krona+One&family=Lexend+Exa:wght@500&family=Montserrat:wght@600;700&display=swap">
<style>
  :root {
    --red: #e5100c;
    --red-dark: #6a0f0d;
    --black: #070808;
    --white: #ffffff;
    --paper: #f7f7f7;
    --stage: #eceeee;
    --photo-blue: #7fb2d8;
    --photo-skin: #b98a6f;
  }
  html, body {
    margin: 0;
    width: 848px;
    height: 1200px;
    overflow: hidden;
    background: var(--stage);
  }
  .banner {
    position: absolute;
    left: 185px;
    top: 0;
    width: 478px;
    height: 1200px;
    background: linear-gradient(180deg, var(--white) 0%, var(--paper) 100%);
    overflow: hidden;
  }
  .banner-shapes {
    position: absolute;
    inset: 0;
  }
  .brand {
    position: absolute;
    left: 0;
    right: 0;
    top: 118px;
    text-align: center;
    font-family: "Montserrat", sans-serif;
    font-weight: 700;
    font-size: 40px;
    letter-spacing: 4px;
    color: var(--black);
  }
  .hero-photo {
    position: absolute;
    left: 240px;
    top: 312px;
    width: 237px;
    height: 226px;
    background: linear-gradient(135deg, #cfe3f1 0%, var(--photo-blue) 55%, #4f86b3 100%);
    clip-path: polygon(0 0, 100% 0, 100% 100%, 55% 100%);
  }
  .headline {
    position: absolute;
    left: 15px;
    top: 366px;
    margin: 0;
    font-weight: normal;
  }
  .headline-accent {
    display: block;
    font-family: "Krona One", sans-serif;
    font-size: 30px;
    color: var(--red);
    line-height: 44px;
  }
  .headline-main {
    display: block;
    font-family: "Lexend Exa", sans-serif;
    font-weight: 500;
    font-size: 31px;
    color: var(--white);
    line-height: 44px;
    margin-top: 14px;
  }
  .specialties {
    position: absolute;
    left: 34px;
    top: 598px;
    margin: 0;
    padding: 0;
    list-style: none;
  }
  .specialty {
    display: flex;
    align-items: center;
    height: 68px;
    font-family: "Krona One", sans-serif;
    font-size: 29px;
    color: var(--red);
    text-shadow: 1px 2px 0 var(--red-dark);
  }
  .specialty-icon {
    width: 42px;
    height: 42px;
    margin-right: 18px;
    flex: none;
  }
  .gallery-photo {
    position: absolute;
    border-radius: 50%;
    border: 3px solid var(--red);
    box-sizing: border-box;
  }
  .gallery-team { left: 31px; top: 831px; width: 150px; height: 150px;
    background: radial-gradient(circle at 55% 40%, var(--photo-skin) 0%, #2a3a78 60%, #dfe3e8 100%); }
  .gallery-hands { left: 165px; top: 815px; width: 150px; height: 150px;
    background: radial-gradient(circle at 40% 45%, #c89a84 0%, #7a4d3c 45%, #7aa3bf 100%); }
  .gallery-care { left: 296px; top: 832px; width: 146px; height: 146px;
    background: radial-gradient(circle at 50% 45%, #9bbfdc 0%, #6d8a8a 50%, #e8ecef 100%); }
  .social {
    position: absolute;
    left: 212px;
    top: 1035px;
    height: 58px;
    display: flex;
    align-items: center;
    font-family: "Montserrat", sans-serif;
    font-weight: 600;
    font-size: 20px;
    color: var(--white);
  }
  .social-dot {
    width: 22px;
    height: 22px;
    border-radius: 50%;
    background: var(--red);
    margin-right: 10px;
  }
  .website {
    position: absolute;
    left: 0;
    right: 0;
    top: 1128px;
    text-align: center;
    font-family: "Lexend Exa", sans-serif;
    font-weight: 500;
    font-size: 19px;
    color: var(--white);
  }
</style>
</head>
<body>
<main class="banner">
  <svg class="banner-shapes" width="478" height="1200" viewBox="0 0 478 1200" aria-hidden="true">
    <defs>
      <linearGradient id="redSweep" x1="0" x2="1" y1="0" y2="0">
        <stop offset="0" stop-color="#6a0f0d"/>
        <stop offset="1" stop-color="#e5100c"/>
      </linearGradient>
      <linearGradient id="redSweepRev" x1="0" x2="1" y1="0" y2="0">
        <stop offset="0" stop-color="#e5100c"/>
        <stop offset="1" stop-color="#6a0f0d"/>
      </linearGradient>
      <linearGradient id="footerRed" x1="0" x2="1" y1="0" y2="0.3">
        <stop offset="0" stop-color="#5e0d0c"/>
        <stop offset="1" stop-color="#e8100c"/>
      </linearGradient>
    </defs>
    <!-- top corner tab -->
    <path d="M0 0 H200 Q178 26 140 28 H0 Z" fill="url(#redSweep)"/>
    <!-- hero band -->
    <path d="M155 312 Q175 288 205 288 H477 V312 Z" fill="url(#redSweepRev)"/>
    <path d="M0 312 H225 Q262 312 282 345 L385 520 Q395 538 380 538 H0 Z" fill="var(--black)"/>
    <rect x="0" y="538" width="477" height="25" fill="var(--black)"/>
    <path d="M125 563 H477 V582 H160 Q138 582 125 563 Z" fill="url(#redSweep)"/>
    <!-- footer -->
    <path d="M0 1003 H140 Q165 1003 180 1025 L230 1100 H477 V1200 H0 Z" fill="url(#footerRed)"/>
    <path d="M175 1035 H477 V1093 H228 Z" fill="var(--black)"/>
  </svg>

  <div class="brand">QUELL STAFFING</div>

  <div class="hero-photo" role="img" aria-label="Photo of a nurse in blue scrubs holding a stethoscope"></div>

  <h1 class="headline">
    <span class="headline-accent">Healthcare</span>
    <span class="headline-main">Recruitment<br>Agency</span>
  </h1>

  <ul class="specialties">
    <li class="specialty">
      <svg class="specialty-icon" viewBox="0 0 42 42" aria-hidden="true"><circle cx="21" cy="21" r="20" fill="var(--red)"/><path d="M17 9h8v8h8v8h-8v8h-8v-8H9v-8h8z" fill="var(--white)"/></svg>
      Allied health
    </li>
    <li class="specialty">
      <svg class="specialty-icon" viewBox="0 0 42 42" aria-hidden="true"><circle cx="21" cy="21" r="20" fill="var(--red)"/><path d="M17 9h8v8h8v8h-8v8h-8v-8H9v-8h8z" fill="var(--white)"/></svg>
      Nursing
    </li>
    <li class="specialty">
      <svg class="specialty-icon" viewBox="0 0 42 42" aria-hidden="true"><circle cx="21" cy="21" r="20" fill="var(--red)"/><path d="M17 9h8v8h8v8h-8v8h-8v-8H9v-8h8z" fill="var(--white)"/></svg>
      Medical imaging
    </li>
  </ul>

  <div class="gallery-photo gallery-team" role="img" aria-label="Photo of a smiling healthcare team in scrubs"></div>
  <div class="gallery-photo gallery-hands" role="img" aria-label="Photo of a carer holding a patient's hands"></div>
  <div class="gallery-photo gallery-care" role="img" aria-label="Photo of a nurse supporting an elderly woman walking"></div>

  <div class="social"><span class="social-dot"></span>@quellstaffing</div>
  <div class="website">www.quellstaffing.com.au</div>
</main>
</body>
</html>
```